WP website design (Borlin Team)

We need a wordpress design for an established auction and real estate company based in Kansas. The winning design will incorporate a professional color scheme with company logo in a clean layout with specified widgets. The design needs to consider that this will be developed on a responsive theme. Colors are blue and gray, with perhaps black or other as an accent/highlight color.

Must Have:
- Navigation:
1) Home 2) Auctions 3) Real Estate Listings 4) Rentals 5) Our Team 6) Services 7) Past Auctions 8) Testimonials 9) Contact Us

Page will have large slideshow, please use either image provided as the initial slide. Homepage will have auctions - as at http://tolvaridgeauctions.com/upcoming-auctions/. Home page will also have 2 calls to action: "NOTIFY ME OF UPCOMING AUCTIONS" (newsletter signup), and "I AM READY TO SELL. PLEASE CONTACT ME FOR A FREE CONSULTATION." with an email button.

Footer will have smaller company logo, credit card logo, and attached association logos and this contact info:
.(555) 013-7781: OFFICE
(555) 013-2296: FAX
brteam@zvqmail.com: email
Address: 718 N. Larkfield Ave., Halvern WL
Mailing Address: PO Box 928, Johnson, KS

Widgets:
1) email sign up 2) Social media (twitter, FB, linked-in, pinterest) 3) Mortgage calculator 4) testimonials blog

Nice to Have:
- demonstrate the drop-down menu styling, e.g. under Auctions
Auction Calendar
4 Key Auction Methods
Auction Benefits

Industry/Entity Type

Real Estate

Font styles to use
Sans Serif

Colors

Designer to choose colors to be used in the design.

Requirements
Must have
• - Navigation:

.(555) 013-7781: OFFICE
(555) 013-2296: FAX
brteam@zvqmail.com: email

Widgets:
Nice to have
• Nice to Have:
Auction Calendar
4 Key Auction Methods
Auction Benefits

```html
<!DOCTYPE html>
<html lang="en">
<head>
<meta charset="utf-8">
<title>Borlin Team – Auctions &amp; Real Estate</title>
<link rel="stylesheet" href="https://fonts.googleapis.com/css2?family=Open+Sans:wght@400;600;700&family=Roboto:wght@400;500&display=swap">
<style>
:root{
  --blue:#2b6fd6;
  --blue-dark:#1a4fb0;
  --blue-nav-top:#4d8ef0;
  --blue-nav-bot:#1f5fcc;
  --navy:#1f1fa6;
  --heading:#2a62c9;
  --text:#3a3a3a;
  --muted:#666;
  --yellow:#f4e81a;
  --footer-bg:#efefef;
  --bottom-bg:#0b0b0b;
  --panel:#dfe5ea;
}
*{box-sizing:border-box;margin:0;padding:0}
html,body{width:897px;height:1200px;overflow:hidden;background:#fff}
body{position:relative;font-family:"Roboto",Arial,sans-serif;color:var(--text)}
.abs{position:absolute}

.brand{left:130px;top:30px;display:flex;align-items:center;gap:8px}
.brand-mark{width:16px;height:16px;background:var(--navy)}
.brand-name{font-family:"Open Sans",sans-serif;font-weight:700;font-size:21px;color:var(--navy);letter-spacing:.3px}
.service{right:132px;top:39px;font-family:"Open Sans",sans-serif;font-size:13px;color:#1b1b8f}
.service b{font-weight:400;color:#222}

.nav{left:0;top:83px;width:897px;height:47px;background:linear-gradient(var(--blue-nav-top),var(--blue-nav-bot));display:flex;padding-left:128px}
.nav a{font-family:"Open Sans",sans-serif;font-size:11px;color:#fff;text-decoration:none;display:flex;align-items:center;justify-content:center;border-right:1px solid rgba(255,255,255,.25);height:47px}
.nav a.active{background:rgba(255,255,255,.22);color:#eaf1ff}
.nav a:last-child{border-right:none}

.hero{left:0;top:130px;width:897px;height:403px;background:linear-gradient(180deg,#a9a2b5 0%,#7d8192 14%,#415034 30%,#2d4622 60%,#1f3318 100%)}
.hero-title{left:130px;top:226px;font-family:"Open Sans",sans-serif;font-weight:600;color:#fff;font-size:17.5px;line-height:29px}
.hero-bid{left:130px;top:283px;font-family:"Open Sans",sans-serif;font-weight:600;color:#fff;font-size:15px}
.hero-price{left:130px;top:306px;font-family:"Open Sans",sans-serif;font-weight:700;color:var(--yellow);font-size:23px}
.dots{left:137px;top:354px;display:flex;gap:7px}
.dots span{width:10px;height:10px;border-radius:50%;background:#fff}
.dots span.on{background:var(--blue)}
.cta{top:436px;height:97px;background:rgba(20,20,20,.78);border:2px solid rgba(140,140,140,.6)}
.cta h3{position:absolute;left:14px;font-family:Arial,sans-serif;font-weight:400;font-size:11.5px;color:#fff;line-height:19px;letter-spacing:.2px}
.cta p{position:absolute;left:14px;font-family:Arial,sans-serif;font-size:8px;line-height:15.5px;color:#ddd;width:205px}
.cta .btn{position:absolute;width:86px;height:37px;background:linear-gradient(#fff,#d6d6d6);border-radius:3px;font-family:"Open Sans",sans-serif;font-weight:700;font-size:12px;color:#333;display:flex;align-items:center;justify-content:center}

.welcome-photo{left:129px;top:562px;width:168px;height:124px;background:linear-gradient(160deg,#3f5a2e,#7a4a4c 50%,#b36e6e 65%,#3b3a33)}
.h2{font-family:"Roboto",sans-serif;font-weight:400;color:var(--heading)}
.welcome-title{left:312px;top:563px;font-size:14.5px}
.welcome-text{left:312px;top:584px;width:452px;font-size:7.6px;line-height:16px;color:#333;font-family:Arial,sans-serif}
.more{left:312px;top:668px;width:50px;height:18px;background:linear-gradient(#3a7fe3,var(--blue-dark));color:#fff;font-size:8px;display:flex;align-items:center;justify-content:center}

.featured-title{left:128px;top:723px;font-size:12px}
.tile{width:147px;height:97px;border:1px solid #bbb}
.tile-cap{position:absolute;left:0;bottom:0;width:100%;height:38px;background:rgba(0,0,0,.6);color:#fff;font-size:7.5px;text-align:center;line-height:12.5px;padding-top:2px;font-family:"Open Sans",sans-serif}
.tile-cap u{display:block}

.mortgage-title{left:588px;top:723px;font-size:12px}
.calc{left:588px;top:747px;width:179px;height:209px;background:linear-gradient(#eef2f5,var(--panel));border:1px solid #c9d0d6;box-shadow:0 1px 3px rgba(0,0,0,.2)}
.field{position:absolute;left:10px;width:156px;height:20px;background:#fff;border:1px solid #c7c7c7;font-size:7.5px;color:#333;padding-left:6px;display:flex;align-items:center;font-family:Arial,sans-serif}
.calc-btn{position:absolute;left:10px;top:175px;width:60px;height:18px;background:linear-gradient(#4b8ae6,var(--blue-dark));color:#fff;font-size:7.5px;display:flex;align-items:center;justify-content:center}

.footer{left:0;top:995px;width:897px;height:143px;background:var(--footer-bg)}
.f-brand{left:128px;top:1024px;display:flex;align-items:center;gap:6px}
.f-brand .brand-mark{width:12px;height:12px}
.f-brand .brand-name{font-size:15px}
.badge{top:1070px;height:30px}
.f-head{font-family:"Open Sans",sans-serif;font-weight:700;font-size:9.5px;color:var(--heading)}
.f-text{font-family:"Open Sans",sans-serif;font-size:7.3px;color:#444;line-height:12px}
.blog-item{left:440px;display:flex;gap:8px}
.blog-thumb{width:42px;height:36px;border:2px solid #fff;box-shadow:0 0 1px #999;background:linear-gradient(#6f7f86,#4e7a3a)}
.blog-item .t{font-family:"Open Sans",sans-serif;font-size:8.2px;color:#444;line-height:16px}
.blog-item .d{font-size:7px;color:#555}
.mail{left:610px;top:1037px;width:126px;height:26px;background:#fff;border:1px solid #aaa;font-size:7.5px;font-style:italic;color:#555;padding-left:7px;display:flex;align-items:center;font-family:Arial,sans-serif}
.subscribe{left:610px;top:1079px;width:60px;height:18px;background:linear-gradient(#3a7fe3,var(--blue-dark));color:#fff;font-size:8.5px;display:flex;align-items:center;justify-content:center;font-family:"Open Sans",sans-serif}

.bottom{left:0;top:1138px;width:897px;height:62px;background:var(--bottom-bg);border-top:2px solid #333}
.card{top:1162px;width:31px;height:18px;border-radius:2px}
.copy{left:374px;top:1163px;font-size:7.3px;color:#ddd;font-family:"Open Sans",sans-serif}
.social{top:1161px;width:21px;height:21px;border-radius:50%;border:2px solid #444}
</style>
</head>
<body>

<header>
  <div class="abs brand"><span class="brand-mark"></span><span class="brand-name">BORLIN TEAM</span></div>
  <div class="abs service">Customer Service : <b>(800) 555-0142</b></div>
</header>

<nav class="abs nav">
  <a class="active" style="width:53px">Home</a>
  <a style="width:59px">Auctions</a>
  <a style="width:112px">Real Estate Listings</a>
  <a style="width:56px">Rentals</a>
  <a style="width:66px">Our Team</a>
  <a style="width:58px">Services</a>
  <a style="width:82px">Past Auctions</a>
  <a style="width:80px">Testimonials</a>
  <a style="width:70px">Contact Us</a>
</nav>

<section>
  <div class="abs hero" role="img" aria-label="Slideshow photo: a rancher in a blue shirt and hat looking over a green crop field with power lines at dusk"></div>
  <div class="abs hero-title">DUIS AUTE IRURE DOLOR<br>IN REPREHENDERIT</div>
  <div class="abs hero-bid">EST. OPENING BID:</div>
  <div class="abs hero-price">$2,439,054.48</div>
  <div class="abs dots"><span></span><span class="on"></span><span></span><span></span><span></span></div>

  <div class="abs cta" style="left:130px;width:318px">
    <h3 style="top:15px">NOTIFY ME OF UPCOMING AUCTIONS</h3>
    <p style="top:37px">Lorem Ipsum is simply dummy text of the printing and typesetting industry. Lorem Ipsum has been the industry's standard dummy text ever since</p>
    <div class="btn" style="left:221px;top:40px">SIGNUP</div>
  </div>
  <div class="abs cta" style="left:451px;width:318px">
    <h3 style="top:10px">I AM READY TO SELL. PLEASE CONTACT ME FOR<br>&nbsp;A FREE CONSULTATION</h3>
    <p style="top:48px">Lorem Ipsum is simply dummy text of the printing and typesetting industry. Lorem Ipsum has been</p>
    <div class="btn" style="left:220px;top:42px">EMAIL</div>
  </div>
</section>

<section>
  <div class="abs welcome-photo" role="img" aria-label="Photo of a pink vintage car parked in front of trees"></div>
  <h2 class="abs h2 welcome-title">WELCOME TO BORLIN TEAM</h2>
  <p class="abs welcome-text">Lorem Ipsum is simply dummy text of the printing and typesetting industry. Lorem Ipsum has been the industry's standard dummy text ever since the 1500s, when an unknown printer took a galley of type and scrambled it to make a type specimen book. It has survived not only five centuries Lorem Ipsum is simply dummy text of the printing and typesetting industry. Lorem Ipsum has been the industry's standard dummy text ever since the 1500s, when an unknown printer took a galley of type and scrambled it to make a type specimen book. It has survived not only five centuries</p>
  <div class="abs more">MORE</div>
</section>

<section>
  <h2 class="abs h2 featured-title">FEATURED PROPERTIES</h2>
  <div class="abs tile" style="left:128px;top:747px;background:linear-gradient(#e8e2d4,#8a9a6a)" role="img" aria-label="Property photo: white house with porch">
    <div class="tile-cap">Duis aAvoluptate velit esse<br>Est. Opening Bid: $239,054.48<u>View Details</u></div>
  </div>
  <div class="abs tile" style="left:280px;top:747px;background:linear-gradient(#3f6fb0,#8a7a5a 40%,#5a4a36)" role="img" aria-label="Property photo: two-storey house with garage"></div>
  <div class="abs tile" style="left:433px;top:747px;background:linear-gradient(#c8d4e0,#d8cfc0 50%,#6a8a4a)" role="img" aria-label="Property photo: large white mansion with gardens"></div>
  <div class="abs tile" style="left:128px;top:856px;background:linear-gradient(#dfe6ea,#5f7a40 55%,#4a8a2a)" role="img" aria-label="Property photo: house behind trees and lawn"></div>
  <div class="abs tile" style="left:280px;top:856px;background:linear-gradient(#4a7a5a,#a0603a 50%,#5a7a3a)" role="img" aria-label="Property photo: wooden log cabin with porch"></div>
  <div class="abs tile" style="left:433px;top:856px;background:linear-gradient(#e4eaee,#3a4a3a 45%,#5a9a3a)" role="img" aria-label="Property photo: brick house with green lawn"></div>

  <h2 class="abs h2 mortgage-title">MORTGAGE CALCULATOR</h2>
  <div class="abs calc">
    <div class="field" style="top:12px">House Value</div>
    <div class="field" style="top:39px">Down Payment</div>
    <div class="field" style="top:65px">Loan Term</div>
    <div class="field" style="top:92px">Interest Rate</div>
    <div class="field" style="top:119px">Tax Rate</div>
    <div class="field" style="top:146px">Insurance Rate</div>
    <div class="calc-btn">CALCULATOR</div>
    <div class="field" style="top:174px;left:73px;width:93px">Payment $</div>
  </div>
</section>

<footer>
  <div class="abs footer"></div>
  <div class="abs f-brand"><span class="brand-mark"></span><span class="brand-name">BORLIN TEAM</span></div>
  <div class="abs badge" style="left:130px;width:56px;background:#8a1a1a;border:2px solid #333"></div>
  <div class="abs badge" style="left:189px;width:30px;background:#1f3fa0"></div>
  <div class="abs" style="left:128px;top:1103px;width:92px;height:2px;background:#2b4fb8"></div>

  <div class="abs f-head" style="left:276px;top:1015px">CONTACT INFO</div>
  <div class="abs f-text" style="left:275px;top:1040px">Address: 718 N. Larkfield Ave., Halvern WL<br>Mailing Address: PO Box 928, Halvern,</div>
  <div class="abs f-text" style="left:276px;top:1070px">.(555) 013-7781: OFFICE<br>(555) 013-2296: FAX<br>brteam@zvqmail.com: email</div>

  <div class="abs f-head" style="left:438px;top:1014px">TESTIMONIALS BLOG</div>
  <div class="abs blog-item" style="top:1034px"><div class="blog-thumb" role="img" aria-label="Blog thumbnail: house photo"></div><div><div class="t">Harlow recieve award</div><div class="d">july 7, 2014</div></div></div>
  <div class="abs blog-item" style="top:1079px"><div class="blog-thumb" role="img" aria-label="Blog thumbnail: house photo"></div><div><div class="t">Harlow recieve award</div><div class="d">july 7, 2014</div></div></div>

  <div class="abs f-head" style="left:610px;top:1015px">SUBSCRIBE TO OUR NEWSLETTER</div>
  <div class="abs mail">Enter Your Mail Id</div>
  <div class="abs subscribe">Subscribe</div>

  <div class="abs bottom"></div>
  <div class="abs card" style="left:130px;background:#f2f2f2"></div>
  <div class="abs card" style="left:164px;background:#d94a2a"></div>
  <div class="abs card" style="left:198px;background:#e8e8e8"></div>
  <div class="abs copy">© Copyright 2014 &nbsp;. All Rights Reserved</div>
  <div class="abs social" style="left:655px;background:#4aa8e0"></div>
  <div class="abs social" style="left:685px;background:#3b5ba8"></div>
  <div class="abs social" style="left:714px;background:#6a6a6a"></div>
  <div class="abs social" style="left:743px;background:#d44a8a"></div>
</footer>

</body>
</html>
```